Business Card design for construction company

I would like a business card design for a construction company - ORD Builders. I have attached the ai logo file for use. I would like the card to be very smart and clean and incorporate only white and the two colours in the logo. I would like the card to have two sides. One side can just have the logo, the other with the relevant information.

Target Market(s)

Building and Construction Clients

Industry/Entity Type

Business

Contact Information for Business Card

Name: Tom Harcliffe
Company: ORD Builders Pty Limited
Address: 14 Mulberry Crescent Oakvale Heights 2093
Phone: 0432 517 208
Email: tomh@ordbuilders.example.au

Font styles to use
Serif
Sans Serif

Requirements
Must have
• Details noted above
• Logo as provided
• Colours as in logo
• Square edges
• A font that compliments the logo
Should not have
• Any colour other than white and those in logo
• Rounded edges

```html
<!DOCTYPE html>
<html lang="en">
<head>
<meta charset="utf-8">
<title>ORD Builders — Business Card</title>
<link rel="stylesheet" href="https://fonts.googleapis.com/css2?family=Michroma&family=Montserrat:wght@400;500&display=swap">
<style>
  :root {
    --stage: #1e2124;
    --brand-blue: #00a9e8;
    --ink: #4a4a4a;
    --ink-soft: #6b6b6b;
    --paper: #ffffff;
  }
  * { box-sizing: border-box; margin: 0; padding: 0; }
  html, body {
    width: 1200px;
    height: 738px;
    overflow: hidden;
    background: var(--stage);
  }
  .canvas {
    width: 1200px;
    height: 738px;
    display: flex;
    align-items: center;
    justify-content: center;
    gap: 40px;
  }
  .card {
    width: 520px;
    height: 318px;
    position: relative;
  }
  .card--front {
    background: var(--brand-blue);
    display: flex;
    align-items: center;
    justify-content: center;
  }
  .card--back {
    background: var(--paper);
  }
  .wordmark {
    font-family: "Michroma", sans-serif;
    font-size: 26px;
    letter-spacing: 2px;
    color: var(--paper);
    white-space: nowrap;
  }
  .card--back .wordmark {
    position: absolute;
    left: 38px;
    top: 60px;
    font-size: 17px;
    letter-spacing: 1.5px;
    color: var(--ink);
  }
  .contact {
    position: absolute;
    left: 292px;
    top: 148px;
    font-family: "Montserrat", sans-serif;
    color: var(--ink-soft);
  }
  .contact__name {
    font-family: "Michroma", sans-serif;
    font-size: 15px;
    letter-spacing: 1px;
    color: var(--brand-blue);
    text-transform: uppercase;
    white-space: nowrap;
  }
  .contact__role {
    font-size: 11px;
    margin-top: 2px;
  }
  .contact__address {
    font-size: 11px;
    line-height: 1.35;
    margin-top: 10px;
    font-style: normal;
  }
  .contact__lines {
    list-style: none;
    margin-top: 10px;
    font-size: 11px;
  }
  .contact__lines li {
    display: flex;
    align-items: center;
    gap: 8px;
    line-height: 1.5;
    white-space: nowrap;
  }
  .contact__icon {
    width: 9px;
    height: 9px;
    fill: var(--brand-blue);
    flex: none;
  }
</style>
</head>
<body>
<main class="canvas">
  <section class="card card--front" aria-label="Card front">
    <span class="wordmark">ORD BUILDERS</span>
  </section>

  <section class="card card--back" aria-label="Card back">
    <span class="wordmark">ORD BUILDERS</span>
    <div class="contact">
      <p class="contact__name">Tom Harcliffe</p>
      <p class="contact__role">President</p>
      <address class="contact__address">14 Mulberry Crescent<br>Oakvale Heights 2093</address>
      <ul class="contact__lines">
        <li>
          <svg class="contact__icon" viewBox="0 0 10 10" aria-hidden="true"><path d="M2 0.5 L3.6 2.4 L2.8 3.6 Q4 6 6.4 7.2 L7.6 6.4 L9.5 8 L8.4 9.5 Q3.5 9 0.5 1.6 Z"/></svg>
          0432 517 208
        </li>
        <li>
          <svg class="contact__icon" viewBox="0 0 10 10" aria-hidden="true"><path d="M0.5 2 H9.5 V8 H0.5 Z M1.5 3 V7 H8.5 V3 L5 5.5 Z" fill-rule="evenodd"/></svg>
          tomh@ordbuilders.example.au
        </li>
      </ul>
    </div>
  </section>
</main>
</body>
</html>
```